Piano-centered Instrumental Jazz Album Needs Cover Artwork

The cover has five parts, each one has obligatory features:

I. Main cover

1. Title: Velvet Keys I.
2. Artist: Marbleway Quartet
3. Design image*

* The main design motive can be something that suggests the number 4 (quartet), the sun (sunlight, sun rays), music, piano, notes, nature… Can, but doesn’t have to be one or more of these. But it should represent what the title says.
* I prefer zen-like, minimalist solutions.
* NO stock images, please! Except for unrecognizable parts of something.

II. Cover inside

1. Track list (18 songs) with durations
2. All songs written by Tibor Renvald
3. Copyright Drelbmusic 2016.
4. Design image

III. Disc

1. Artist: Marbleway Quartet
2. Title: Velvet Keys I.
3. All songs written by Tibor Renvald (round on the edge)
4. Copyright Drelbmusic 2016. (round on the edge)
5. www.drelbmusic.com (round on the edge)

IV. Cover back

1. Track list (same as cover inside)
4. www.drelbmusic.com
5. design image (optional)
6. The paper of this page is longer than the main cover, because it is to be turned up when put in the CD case, and there is the saddle with the name of the Artist and Title of the album. On both ends.

V. Under the disc

1. No words, only some design feature.

Important:
The main cover I need in RGB and also CMYK, all the others only CMYK.
I need the work file (cdr, ai or whatever you use)
I need the CMYK images prepared for printing (sizes set, and that little extra on the edges).
I need the RGB main cover cover in jpeg, 3000x3000 pixels.
That's all. :)

The most important of these all is of course the main cover RGB. Do this one first!

Here’s a sample to listen, it might inspire you:

https://files.vexlorahost.net/u/83047162/marbleway%20quartet%20sample%2020160103.mp3

If you take a closer look at my website, you can see the whole concept.

Good luck and enjoy!
Regards,
Tibor

Requirements
Must have
• Tracklist:
• 1 First, in G 05:08
• 2 Second, in Em 05:11
• 3 Third, in G 05:09
• 4 Fourth, in A 05:07
• 5 Fifth, in Bm 05:01
• 6 Sixth, in A 05:11
• 7 Seventh, in G 05:07
• 8 Eighth, in Bm 05:06
• 9 Ninth, in Gm 05:04
• 10 Tenth, in E 05:03
• 11 Eleventh, in G 05:12
• 12 Twelfth, in A 05:09
• 13 Thirteenth, in E 05:10
• 14 Fourteenth, in Am 05:14
• 15 Fifteenth, in F 05:05
• 16 Sixteenth, in Am 05:05
• 17 Seventeenth, in F 05:04
• 18 Eighteenth, in D 05:07
Should not have
• Stock images copy-pasted, additional copyright costs.

```html
<!DOCTYPE html>
<html lang="en">
<head>
<meta charset="utf-8">
<title>Velvet Keys I. — Marbleway Quartet</title>
<link rel="stylesheet" href="https://fonts.googleapis.com/css2?family=Michroma&display=swap">
<style>
  :root {
    --page-bg: #ececec;
    --cover-deep: #021a0c;
    --cover-mid: #0a4a24;
    --cover-glow: #1f7a3c;
    --key-light: #d9f0a0;
    --key-green: #3e9a4c;
    --title-ink: #f2f5f2;
    --artist-ink: #6f7f74;
  }
  * { margin: 0; padding: 0; box-sizing: border-box; }
  html, body {
    width: 1200px;
    height: 848px;
    overflow: hidden;
    background: var(--page-bg);
  }
  .album-cover {
    position: absolute;
    left: 220px;
    top: 44px;
    width: 760px;
    height: 760px;
    overflow: hidden;
    background:
      radial-gradient(ellipse 60% 45% at 70% 100%, rgba(120,200,90,0.35), transparent 70%),
      linear-gradient(100deg, transparent 20%, rgba(40,120,60,0.25) 35%, transparent 50%, rgba(40,120,60,0.2) 65%, transparent 80%),
      linear-gradient(180deg, var(--cover-deep) 0%, #03250f 35%, var(--cover-mid) 70%, var(--cover-glow) 100%);
  }
  .album-title {
    position: absolute;
    left: 0;
    right: 0;
    top: 282px;
    text-align: center;
    font-family: "Michroma", sans-serif;
    font-weight: 400;
    font-size: 30px;
    letter-spacing: 0.55em;
    padding-left: 0.55em;
    color: var(--title-ink);
    line-height: 1;
  }
  .album-artist {
    position: absolute;
    left: 0;
    right: 0;
    top: 318px;
    text-align: center;
    font-family: "Michroma", sans-serif;
    font-weight: 400;
    font-size: 24px;
    letter-spacing: 0.62em;
    padding-left: 0.62em;
    color: var(--artist-ink);
    line-height: 1;
    opacity: 0.8;
  }
  .keys-artwork {
    position: absolute;
    left: 0;
    bottom: 0;
    width: 100%;
    height: 200px;
    background:
      radial-gradient(ellipse 30% 70% at 68% 85%, var(--key-light), transparent 70%),
      linear-gradient(180deg, rgba(20,80,40,0) 0%, var(--key-green) 55%, #cfe6d8 100%);
  }
</style>
</head>
<body>
  <main class="album-cover">
    <h1 class="album-title">VELVET KEYS I</h1>
    <p class="album-artist">MARBLEWAY QUARTET</p>
    <div class="keys-artwork" role="img" aria-label="Close-up of piano keys in soft green light, blurred toward a bright glow on the right"></div>
  </main>
</body>
</html>
```